Harbinger Noble Alloys Works Business Cards

We are wanting to have a new business card designed for our company as we go to a convention. We want to balance business/Modern with elegance and beauty. Our company sells highend jewelry pieces. We want to utilize the colors of Black and Gold and have gold foiled fonts to be physically printed on the business cards.
We also would like to have space to write notes on the back side of the business card. When we meet people at jewelry conventions we would like to write notes if possible.
Here are websites and designs that we like the look and feel of these companies and you can use these as design ideas.
https://www.lorvanne.com
https://www.bellquist.com/en-us/home
Here is our company website link
www.harbingernaw.com
I also up loaded two versions of our logo.
- Update 4.26.22
I have uploaded photos of a business card we like. this card has raised embossed letters that you can feel. the raise letters are like a plastic but we don't need to use that...I uploaded to show you that we like the experience of the client feeling the characters of the logo. we also would like to have the material as a satin or some material very soft.
- Maybe we can get designs with beautiful gold foiling and raised characters and logos. we like simplicity...not busy but an elegant design. We need to write notes and would like a section where we can write notes. but we want an elegant style and the client has an experience with the feel of the card when they touch the card.
Colors
- Main colors Black & Gold
- white or light colors for small notes section.
Specialty ideals and things we would like to see based on your design styles.
- raised fonts
- raised logos
- gold foiling
- satin/soft finish on the card material.
we are wanting to design a business card that looks elegant and clean. When the client is handed the business card we want them to physically experience the business card as well by touching the raised logos or fonts and the base material is soft satin. I hope this helps with further designs.
thank you all
We uploaded a new contact layout that we have designed in our office. we would like to see how this would look on your designs.
thank you
I just finished uploading the Contact Layout. the colors are just examples. please use this layout as an idea and use colors based on the feed back we have given each of you personally.
Contact Information for Business Card
we need an area to write notes, we would like to have our logos or the diamond of our logo or the business card to have embossed sections to the business card so when the customer touches the card they can feel the logo. we would also like sections of our business card to have gold foiling. we would also like to use a satin soft paper with our card. when the client touches the card its super soft and high quality
Requirements
Must have
- we would like to have our logos or the diamond of our logo or the business card to have embossed sections to the business card so when the customer touches the card they can feel the logo. we would also like sections of our business card to have gold foiling. we would also like to use a satin soft paper with our card. when the client touches the card its super soft and high quality
Nice to have
- we would like to have our logos or the diamond of our logo or the business card to have embossed sections to the business card so when the customer touches the card they can feel the logo. we would also like sections of our business card to have gold foiling.

```html
<!DOCTYPE html>
<html lang="en">
<head>
<meta charset="utf-8">
<title>Harbinger Noble Alloys Works – Business Cards</title>
<link rel="stylesheet" href="https://fonts.googleapis.com/css2?family=Cinzel:wght@500&family=Montserrat:wght@500;700&display=swap">
<style>
  :root {
    --backdrop: #d8d3cf;
    --paper: #fbfaf7;
    --ink-black: #07090a;
    --gold: #c49a45;
    --gold-soft: #d6b46a;
  }
  * { box-sizing: border-box; margin: 0; padding: 0; }
  html, body { width: 1200px; height: 957px; overflow: hidden; }
  body {
    background: var(--backdrop);
    position: relative;
    font-family: "Montserrat", Arial, sans-serif;
  }
  .card {
    position: absolute;
    width: 520px;
    height: 298px;
    border-radius: 3px;
    box-shadow: 0 10px 30px rgba(60, 45, 30, 0.18);
  }
  .card--front { left: 50px; top: 330px; background: var(--paper); }
  .card--back  { left: 630px; top: 330px; background: var(--ink-black); }

  .wordmark {
    font-family: "Cinzel", Georgia, serif;
    font-weight: 500;
    color: var(--gold);
    text-align: center;
    letter-spacing: 0.02em;
    display: flex;
    align-items: center;
    justify-content: center;
    gap: 10px;
  }
  .wordmark__dot {
    width: 10px; height: 10px;
    border-radius: 50%;
    background: var(--gold);
    flex: none;
  }
  .card--front .wordmark { position: absolute; top: 44px; left: 0; right: 0; font-size: 21px; }
  .card--back .wordmark {
    position: absolute; top: 0; bottom: 0; left: 0; right: 0;
    font-size: 27px; flex-direction: column; gap: 18px;
  }
  .card--back .wordmark__dot { width: 16px; height: 16px; }

  .holder { position: absolute; top: 100px; left: 0; right: 0; text-align: center; color: var(--gold); }
  .holder__name { font-weight: 700; font-size: 19px; }
  .holder__title { font-weight: 500; font-size: 9px; margin-top: 2px; }

  .rule { position: absolute; left: 32px; right: 32px; height: 1px; background: var(--gold-soft); }
  .rule--top { top: 88px; }
  .rule--bottom { top: 252px; }

  .contacts {
    position: absolute; top: 160px; left: 32px; right: 32px;
    display: grid; grid-template-columns: 1fr 1.3fr 1fr;
    color: var(--gold); font-weight: 700; font-size: 12px;
  }
  .contacts__col { display: flex; flex-direction: column; gap: 7px; }
  .contacts__col--end { align-items: flex-end; }
  .contact { display: flex; align-items: center; gap: 6px; white-space: nowrap; }
  .contact svg { width: 10px; height: 10px; flex: none; fill: none; stroke: var(--gold); stroke-width: 1.6; }
</style>
</head>
<body>
  <section class="card card--front" aria-label="Business card front">
    <div class="wordmark"><span class="wordmark__dot"></span>Harbinger Noble Alloys Works</div>
    <div class="rule rule--top"></div>
    <div class="holder">
      <p class="holder__name">Name Here</p>
      <p class="holder__title">Title Here</p>
    </div>
    <div class="contacts">
      <div class="contacts__col">
        <span class="contact"><svg viewBox="0 0 10 10"><rect x="2.5" y="0.8" width="5" height="8.4" rx="1"/></svg>000 000 0000</span>
      </div>
      <div class="contacts__col">
        <span class="contact"><svg viewBox="0 0 10 10"><path d="M1 3.5c0-1.5 8-1.5 8 0v1.2H7V3.8H3v0.9H1z M2 5.5h6v3H2z"/></svg>000 000 0000</span>
        <span class="contact"><svg viewBox="0 0 10 10"><rect x="0.8" y="2" width="8.4" height="6"/><path d="M0.8 2l4.2 3.4L9.2 2"/></svg>info@harbingernaw.com</span>
        <span class="contact"><svg viewBox="0 0 10 10"><circle cx="5" cy="5" r="4"/><path d="M1 5h8M5 1c2 2.5 2 5.5 0 8M5 1c-2 2.5-2 5.5 0 8"/></svg>www.harbingernaw.com</span>
      </div>
      <div class="contacts__col contacts__col--end">
        <span class="contact"><svg viewBox="0 0 10 10"><rect x="1" y="3.5" width="8" height="5"/><path d="M3 3.5V1h4v2.5"/></svg>000 000 0000</span>
      </div>
    </div>
    <div class="rule rule--bottom"></div>
  </section>

  <section class="card card--back" aria-label="Business card back">
    <div class="wordmark"><span class="wordmark__dot"></span>Harbinger Noble Alloys Works</div>
  </section>
</body>
</html>
```